Commercial Construction Interior Fitout company needs Logo and Business Cards

We need a logo and business card design. We specialise in Commercial Ceilings, Partitions, Plastering and Carpentry.

Company name: 7QX Commercial Interiors. Would like a professional looking card more than a fancy look. Gloss front preferably black pattern with Fluro Green and white text.

Will need:

Name
Position
Phone
Fax
Email
Postal Address
Web address
Updates

Thank you so much everyone for your efforts and fantastic designs..   If I didn't respond to everyone personally,  my apologises. 

Again, thanks all

R.M                               

Target Market(s)

Existing & New clients in the Construction Industry

Industry/Entity Type

Business

Requirements
Nice to have
• 7QX to be overlapped or made into some sort of Logo

```html
<!DOCTYPE html>
<html lang="en">
<head>
<meta charset="utf-8">
<title>7QX Commercial Interiors – Business Card</title>
<link href="https://fonts.googleapis.com/css2?family=Quicksand:wght@500;600;700&display=swap" rel="stylesheet">
<style>
  :root {
    --backdrop: #242122;
    --card-white: #ffffff;
    --fluro-green: #7fcb6a;
    --brand-green: #1f7a2a;
    --ink: #222222;
    --band-dark: #3d3d3d;
  }
  * { box-sizing: border-box; margin: 0; padding: 0; }
  html, body { width: 1200px; height: 708px; overflow: hidden; }
  body {
    background: var(--backdrop);
    font-family: "Quicksand", "Century Gothic", sans-serif;
    color: var(--ink);
    position: relative;
  }
  .card {
    position: absolute;
    width: 540px;
    height: 318px;
    overflow: hidden;
  }
  .card-front {
    left: 40px; top: 60px;
    background: var(--card-white);
    border-radius: 6px 36px 6px 36px;
  }
  .front-band {
    height: 20px;
    background: var(--fluro-green);
    border-bottom: 6px solid var(--band-dark);
  }
  .front-title {
    text-align: center;
    font-size: 33px;
    font-weight: 600;
    margin-top: 12px;
    letter-spacing: 0.5px;
  }
  .contact-block {
    position: absolute;
    left: 30px; top: 120px;
  }
  .person-name { font-size: 19px; font-weight: 700; }
  .person-role { font-size: 14px; font-weight: 500; margin-left: 24px; margin-bottom: 12px; }
  .contact-list { list-style: none; font-size: 12px; font-weight: 500; }
  .contact-list li { display: flex; align-items: center; height: 19px; }
  .contact-list svg { width: 12px; height: 12px; margin-right: 14px; fill: var(--ink); }
  .brand-mark {
    position: absolute;
    right: 36px; top: 112px;
    text-align: center;
  }
  .brand-mark .brand-name {
    font-size: 108px;
    font-weight: 700;
    line-height: 1;
    color: var(--brand-green);
    letter-spacing: 2px;
  }
  .brand-mark .brand-tagline {
    font-size: 25px;
    font-weight: 500;
    margin-top: 4px;
    text-align: right;
  }
  .card-back {
    left: 620px; top: 330px;
    background: var(--fluro-green);
    border-radius: 30px;
    display: flex;
    flex-direction: column;
    align-items: center;
    justify-content: center;
  }
  .card-back .brand-name {
    font-size: 76px;
    font-weight: 700;
    line-height: 1;
    color: var(--brand-green);
    letter-spacing: 2px;
  }
  .card-back .brand-tagline {
    font-size: 21px;
    font-weight: 500;
    color: #1d3a1a;
    margin-top: 2px;
  }
  .card-back .brand-web {
    font-size: 12px;
    font-weight: 500;
    color: #1d3a1a;
    margin-top: 10px;
  }
</style>
</head>
<body>
  <section class="card card-front">
    <div class="front-band"></div>
    <h1 class="front-title">7QX Commercial Interiors</h1>

    <div class="contact-block">
      <p class="person-name">Name/Owner</p>
      <p class="person-role">Director</p>
      <ul class="contact-list">
        <li><svg viewBox="0 0 24 24"><path d="M6.6 10.8a15 15 0 0 0 6.6 6.6l2.2-2.2a1 1 0 0 1 1-.25 11.4 11.4 0 0 0 3.6.57 1 1 0 0 1 1 1V20a1 1 0 0 1-1 1A17 17 0 0 1 3 4a1 1 0 0 1 1-1h3.5a1 1 0 0 1 1 1c0 1.25.2 2.45.57 3.57a1 1 0 0 1-.25 1z"/></svg>0000000000061 ext.111</li>
        <li><svg viewBox="0 0 24 24"><circle cx="12" cy="12" r="11"/><rect x="9" y="6" width="6" height="12" rx="1" fill="#fff"/></svg>0000000000</li>
        <li><svg viewBox="0 0 24 24"><path d="M2 5h20v14H2z"/><path d="M2 5l10 8 10-8" fill="none" stroke="#fff" stroke-width="2"/></svg>info@7qx.net</li>
        <li><svg viewBox="0 0 24 24"><path d="M12 1a8 8 0 0 0-8 8c0 6 8 14 8 14s8-8 8-14a8 8 0 0 0-8-8zm0 11a3 3 0 1 1 0-6 3 3 0 0 1 0 6z"/></svg>Adress xxxxxxx</li>
        <li><svg viewBox="0 0 24 24"><circle cx="12" cy="12" r="11"/><circle cx="12" cy="12" r="6" fill="#fff"/><circle cx="12" cy="12" r="3"/></svg>www.7qx.net</li>
      </ul>
    </div>

    <div class="brand-mark">
      <p class="brand-name">7QX</p>
      <p class="brand-tagline">Commercial Interiors</p>
    </div>
  </section>

  <section class="card card-back">
    <p class="brand-name">7QX</p>
    <p class="brand-tagline">Commercial Interiors</p>
    <p class="brand-web">www.7qx.net</p>
  </section>
</body>
</html>
```